NZ First of it's kind solutions directory and marketplace for busy Mums needs a business card design

We need a business card design for our new nationwide business in NZ (long term plans to go global). We provide solutions to the everyday challenges that busy Mums face by connecting them with quality communities and suppliers of carefully selected, relevant products and services. We sell direct via our online marketplace. The final design should communicate our values of inclusivity, quality and smart solutions. Colours should incorporate our logo colour palette of #477077 and #6ba8b2. Our website is at https://www.brightnestly.com

Target Market(s)

busy Mums, Age 28 – 50, female, income over $100K, location main centres NZ primarily but NZ wide. Is likely juggling work or career with a young family. Probably had hobbies which have fallen by the wayside.
-Wants to succeed in her chosen career without compromising on family life
-to successfully juggle her career without feeling like she is compromising her children
- Is time poor, something always has to give and it’s generally her health (she’ll stay up late, get stressed)
- probably ex corporate or professional career. Has discretional income

Industry/Entity Type

Business

Contact Information for Business Card

Jodie Farnsworth, Founder, BrightNestly.com (Strapline Browse; Pick; Sorted), 48 Kowhai Terrace, Hillsborough, Auckland 1058, New Zealand. Mob: 021 437 518 Ph: +64 (0)9 584 7163

Font styles to use
Other font styles liked:
• Raleway, and/or Architects Daughter

Colors
00a990
33b8a4
86cfc6
cfeae6

Requirements
Must have
• the above details, streamline. the logo and colours associated with those logos
Should not have
• foil or metallic colours

```html
<!DOCTYPE html>
<html lang="en">
<head>
<meta charset="utf-8">
<title>BrightNestly Business Card</title>
<link rel="stylesheet" href="https://fonts.googleapis.com/css2?family=Jost:wght@400;500&display=swap">
<style>
  :root {
    --teal-deep: #4f7479;
    --teal-light: #6fa9b2;
    --mist: #a9bac0;
    --card-edge: #d6d9da;
    --paper: #ffffff;
  }
  * { box-sizing: border-box; margin: 0; padding: 0; }
  html, body {
    width: 1200px; height: 1200px; overflow: hidden;
    background: var(--paper);
    font-family: "Jost", sans-serif;
  }
  .canvas { position: relative; width: 1200px; height: 1200px; }
  .card {
    position: absolute; left: 283px; width: 647px; height: 418px;
    border: 1px solid var(--card-edge); border-radius: 24px;
    overflow: hidden; background: var(--paper);
  }
  .card--front { top: 145px; }
  .card--back { top: 636px; }

  .brand {
    position: absolute; left: 0; right: 0; top: 120px;
    display: flex; align-items: center; justify-content: center; gap: 20px;
  }
  .brand__dot {
    width: 56px; height: 56px; border-radius: 50%;
    background: var(--teal-light);
  }
  .brand__name {
    font-weight: 500; font-size: 64px; letter-spacing: -0.5px;
    color: var(--teal-deep); line-height: 1;
  }
  .web-band {
    position: absolute; left: 0; right: 0; bottom: 0; height: 90px;
    background: var(--teal-light);
    display: flex; align-items: center; justify-content: center;
  }
  .web-band__url {
    color: var(--paper); font-size: 22px; letter-spacing: 0.32em;
    font-weight: 400; padding-left: 0.32em;
  }

  .feature-panel {
    position: absolute; left: 0; top: 0; width: 290px; height: 100%;
  }
  .contact {
    position: absolute; right: 34px; top: 84px;
    text-align: right; color: var(--teal-deep);
  }
  .contact__name { font-size: 34px; font-weight: 400; line-height: 1.1; }
  .contact__rule {
    width: 304px; height: 3px; background: var(--teal-light);
    margin: 6px 0 6px auto;
  }
  .contact__role {
    font-size: 22px; font-variant: small-caps; letter-spacing: 0.04em;
    line-height: 1.2;
  }
  .contact__details {
    margin-top: 46px; font-size: 22px; line-height: 30px;
  }
  .contact__label { color: var(--teal-light); }
</style>
</head>
<body>
<main class="canvas">
  <section class="card card--front">
    <div class="brand">
      <span class="brand__dot"></span>
      <span class="brand__name">BrightNestly</span>
    </div>
    <div class="web-band">
      <span class="web-band__url">WWW.BRIGHTNESTLY.COM</span>
    </div>
  </section>

  <section class="card card--back">
    <svg class="feature-panel" role="img" aria-label="Large brand emblem decoration in deep and soft teal tones" viewBox="0 0 290 418" preserveAspectRatio="none">
      <defs>
        <linearGradient id="panelTone" x1="0" y1="0" x2="1" y2="1">
          <stop offset="0" stop-color="#4f7479"/>
          <stop offset="1" stop-color="#a9bac0"/>
        </linearGradient>
      </defs>
      <rect width="290" height="418" fill="url(#panelTone)"/>
    </svg>
    <div class="contact">
      <h1 class="contact__name">Jodie Farnsworth</h1>
      <div class="contact__rule"></div>
      <p class="contact__role">Founder</p>
      <address class="contact__details" style="font-style:normal">
        48 Kowhai Terrace,<br>
        Hillsborough, Auckland 1058,<br>
        New Zealand.<br>
        <span class="contact__label">Mob:</span> 021 437 518<br>
        <span class="contact__label">Ph:</span> +64 (0)9 584 7163
      </address>
    </div>
  </section>
</main>
</body>
</html>
```